Flyer for American Indian Elders on Dementia Warning Signs

We need a flyer designed for older adults who are American Indian or Alaska Native (in the U.S.).

Ideally, the flyer should complement the colors of our logos. The project logo and our organization logo are attached to the brief.

When people see the flyer we want them to feel that it represents their culture, is warm, and professional but relatable to older adults and people who have limited incomes.

I have attached an earlier draft of the document we designed ourselves BUT we want different and better.

It is for older adults who have trouble reading so:
1. you must use a font that is 11.5 points or larger
2. Do not put text over complex pictures or use shading with words
3. You can use a serif font for the heading, but should use san serif for the body text
4. There should be good contrast between the font color and background

Please do not use any images that include a head dress or pictures of American Indian people or things that are very traditional or "token" imagery.

We need to save a small space under the call out box/ somewhere on the flyer for other people to add their logo once they download.

Let us know if you have questions or need additional information.

Target Market(s)

Older American Indian people

Font styles to use
Serif
Sans Serif

Requirements
Must have
• Easy to read for older adults
Should not have
• indian headdress

```html
<!DOCTYPE html>
<html lang="en">
<head>
<meta charset="utf-8">
<title>10 Signs of Thinking or Memory Changes That Might Be Dementia</title>
<link rel="stylesheet" href="https://fonts.googleapis.com/css2?family=Bebas+Neue&family=Oswald:wght@300;500&family=Quicksand:wght@600;700&display=swap">
<style>
  :root {
    --teal: #5ba8b1;
    --teal-deep: #3e9aa4;
    --teal-dark: #2a8b90;
    --rust: #b35a4f;
    --cream: #f7f0dc;
    --paper: #ffffff;
    --mist: #e1eaec;
    --grey: #b5b5b5;
  }
  * { margin: 0; padding: 0; box-sizing: border-box; }
  html, body { width: 848px; height: 1200px; overflow: hidden; background: var(--paper); }
  .flyer { position: relative; width: 848px; height: 1200px; overflow: hidden; background: var(--paper); font-family: "Quicksand", sans-serif; }
  .backdrop { position: absolute; inset: 0; }
  .top-rule { position: absolute; left: 0; top: 0; width: 848px; height: 12px; background: var(--rust); }

  .org { position: absolute; top: 50px; display: flex; align-items: center; gap: 8px; }
  .org-primary { left: 42px; }
  .org-primary .dot { width: 30px; height: 30px; background: var(--teal-deep); }
  .org-primary .name { font-family: "Bebas Neue", sans-serif; color: var(--rust); font-size: 21px; line-height: 0.95; border-left: 2px solid var(--teal-deep); padding-left: 8px; }
  .org-primary .name small { display: block; color: var(--teal-deep); font-size: 14px; }
  .org-partner { left: 370px; }
  .org-partner .dot { width: 30px; height: 30px; border-radius: 50%; background: var(--teal-deep); }
  .org-partner .name { font-family: "Bebas Neue", sans-serif; color: var(--teal-deep); font-size: 17px; line-height: 0.95; }

  .big-number { position: absolute; left: 36px; top: 110px; font-family: "Bebas Neue", sans-serif; font-size: 146px; line-height: 1; color: var(--teal-deep); letter-spacing: -4px; }
  .headline { position: absolute; left: 144px; top: 128px; font-family: "Bebas Neue", sans-serif; font-size: 37px; line-height: 0.86; color: var(--teal-deep); font-weight: 400; }

  .intro { position: absolute; left: 40px; top: 242px; width: 498px; height: 82px; background: var(--paper); border: 2px solid var(--teal-deep); padding: 8px 9px; font-family: "Bebas Neue", sans-serif; font-size: 21.5px; line-height: 0.98; color: var(--rust); }

  .banner { position: absolute; left: 579px; top: 12px; width: 228px; height: 294px; background: var(--rust); border-bottom: 8px solid var(--teal-dark); padding: 30px 18px 0 32px; font-family: "Bebas Neue", sans-serif; font-size: 19.5px; line-height: 1.1; color: var(--cream); }

  .col-rule { position: absolute; top: 346px; width: 1px; height: 777px; background: rgba(255,255,255,0.45); }
  .row-rule { position: absolute; height: 1px; background: rgba(255,255,255,0.45); }

  .sign { position: absolute; color: var(--cream); font-size: 15.6px; line-height: 22.8px; font-weight: 600; letter-spacing: 0.4px; }
  .sign .lead { display: flex; }
  .sign .num { width: 20px; flex: none; }
  .sign ul { list-style: none; }
  .sign li { display: flex; }
  .sign li::before { content: "›"; width: 20px; flex: none; padding-left: 1px; }

  .main-points { position: absolute; left: 580px; top: 577px; width: 227px; height: 451px; }
  .main-points svg { position: absolute; inset: 0; }
  .main-points h2 { position: absolute; left: 0; right: 0; top: 15px; text-align: center; font-family: "Bebas Neue", sans-serif; font-weight: 400; font-size: 42px; color: var(--teal-deep); }
  .main-points .rule { position: absolute; left: 40px; right: 40px; top: 60px; height: 1px; background: var(--teal); }
  .main-points .points { position: absolute; left: 10px; right: 10px; top: 81px; text-align: center; color: var(--teal-deep); font-size: 13.6px; line-height: 17.2px; font-weight: 700; }
  .main-points p + p { margin-top: 17px; }

  .logo-slot { position: absolute; left: 653px; top: 1121px; font-family: "Bebas Neue", sans-serif; font-size: 41px; color: var(--grey); letter-spacing: 0.5px; }

  .footer { position: absolute; left: 42px; top: 1142px; width: 496px; height: 70px; background: var(--paper); border: 2px solid var(--teal-deep); padding: 7px 7px; font-family: "Oswald", sans-serif; font-weight: 300; font-size: 12.4px; line-height: 1.1; color: var(--teal-deep); text-transform: uppercase; }
  .footer strong { font-weight: 500; }
</style>
</head>
<body>
<main class="flyer">
  <svg class="backdrop" width="848" height="1200" viewBox="0 0 848 1200" aria-hidden="true">
    <polygon points="0,342 848,107 848,1021 434,1139 434,1200 0,1200" fill="var(--teal)"/>
  </svg>
  <div class="top-rule"></div>

  <div class="org org-primary"><span class="dot"></span><span class="name"><small>Council for</small>Native Elder Wellness</span></div>
  <div class="org org-partner"><span class="dot"></span><span class="name">Native Elders<br>Brain Health Circle</span></div>

  <div class="big-number">10</div>
  <h1 class="headline">Signs of thinking or<br>memory changes that<br>might be dementia</h1>

  <p class="intro">Because American Indian and Alaska Native people have a high risk of dementia, it is important to know the warning signs. Do you have any of these 10 signs? If so, talk to your doctor.</p>

  <p class="banner">As we get older, we may slow down a bit. This is a normal part of aging. Changes in memory or thinking that make it harder to get through the day, are not a normal part of aging. These may be early signs of dementia.</p>

  <div class="col-rule" style="left:289px"></div>
  <div class="col-rule" style="left:557px"></div>
  <div class="row-rule" style="left:0;width:287px;top:540px"></div>
  <div class="row-rule" style="left:0;width:287px;top:698px"></div>
  <div class="row-rule" style="left:0;width:287px;top:794px"></div>
  <div class="row-rule" style="left:0;width:287px;top:926px"></div>
  <div class="row-rule" style="left:292px;width:263px;top:541px"></div>
  <div class="row-rule" style="left:292px;width:263px;top:699px"></div>
  <div class="row-rule" style="left:297px;width:258px;top:880px"></div>

  <section class="sign" style="left:41px;top:346px;width:246px">
    <div class="lead"><span class="num">1.</span><span>Memory loss that affects your daily life. You may:</span></div>
    <ul><li>Forget events or import-<br>ant dates</li><li>Repeat yourself</li><li>Rely more often on lists or sticky notes to remember things</li></ul>
  </section>
  <section class="sign" style="left:41px;top:551px;width:246px">
    <div class="lead"><span class="num" style="width:25px">2.</span><span>Trouble planning or solving problems. You may have a harder time:</span></div>
    <ul><li>Paying bills</li><li>Cooking recipes you have used for years</li></ul>
  </section>
  <section class="sign" style="left:41px;top:710px;width:246px">
    <div class="lead"><span class="num">3.</span><span>Get confused about the time, date, or where you are.</span></div>
  </section>
  <section class="sign" style="left:41px;top:801px;width:246px">
    <div class="lead"><span class="num">4.</span><span>Daily tasks are getting harder, including:</span></div>
    <ul><li>Driving</li><li>Making a grocery list or going shopping</li></ul>
  </section>
  <section class="sign" style="left:41px;top:938px;width:246px">
    <div class="lead"><span class="num">5.</span><span>Trouble with how your eyesight and thinking work together that gets worse. This includes:</span></div>
    <ul><li>Tripping, falls, or prob-<br>lems with your balance</li><li>Spilling or dropping things more</li></ul>
  </section>

  <section class="sign" style="left:310px;top:346px;width:246px">
    <div class="lead"><span class="num">6.</span><span>New trouble talking or writing. You have a hard time finding the words you want to say. For example, you may say “that thing on your wrist that tells time” instead of “watch.”</span></div>
  </section>
  <section class="sign" style="left:310px;top:551px;width:246px">
    <div class="lead"><span class="num">7.</span><span>Lose and cannot find things. For example, you:</span></div>
    <ul><li>Can’t find the coffee pot that you use every day</li><li>Might put your car keys in the freezer</li></ul>
  </section>
  <section class="sign" style="left:310px;top:710px;width:246px">
    <div class="lead"><span class="num">8.</span><span>Notice changes in mood or personality, such as being:</span></div>
    <ul><li>Easily mad or sad in ev-<br>eryday situations</li><li>More fearful (scared) or suspicious (not trusting)</li></ul>
  </section>
  <section class="sign" style="left:310px;top:892px;width:246px">
    <div class="lead"><span class="num">9.</span><span>Act different and make poor choices. This may make you more likely to:</span></div>
    <ul><li>Spend money you do not have or be a scam victim</li><li>Stop washing up regular-<br>ly or pay less attention to how you look</li></ul>
  </section>

  <section class="sign" style="left:580px;top:346px;width:232px">
    <ul><li>Forget to take care of your pet</li></ul>
    <div class="lead"><span class="num" style="width:24px">10.</span><span>Pull away from friends and family because it is harder to keep up. You may not want to do things you used to en-<br>joy, like sporting events, church, music, or sex.</span></div>
  </section>

  <aside class="main-points">
    <svg width="227" height="451" viewBox="0 0 227 451" aria-hidden="true">
      <polygon points="20,1 207,1 226,20 226,431 207,450 20,450 1,431 1,20" fill="var(--mist)" stroke="var(--teal-deep)" stroke-width="1.5" stroke-dasharray="2 2"/>
      <line x1="6" y1="424" x2="221" y2="424" stroke="var(--teal)" stroke-width="0.8"/>
    </svg>
    <h2>Main Points</h2>
    <div class="rule"></div>
    <div class="points">
      <p>American Indian and Alaska Native people have a high risk of dementia.</p>
      <p>Big changes in memory or thinking that make it hard to get through the day are not a normal part of aging.</p>
      <p>People with one or more of these 10 signs should talk to their doctor to find the cause. It is not always dementia.</p>
      <p>Early dementia diagnosis gives you a chance to get care and plan your future.</p>
    </div>
  </aside>

  <div class="logo-slot">Logo Here</div>

  <p class="footer">To learn more about the warning signs of dementia in American Indian and Alaska Native people, visit: <strong>www.nativeeldersbrain.org, www.healthyagingnet.org/elders</strong></p>
</main>
</body>
</html>
```